Looking for a design of labels for canned mushrooms for the brand Mira Pomel.

We have to find a label for two types of mushrooms. One is for sliced ​​mushrooms and the other one is for whole mushrooms. This project is for Mira Pomel, a company working in the food industry, Velunda, who is also a canned food company. The product is marketed for North America. What we want on the label: - the nutrition facts; - the list of ingredients (mushrooms, water, salt, citric acid); - the weight: 200 g; - For the first one: "Sliced ​​Mushrooms / Sliced ​​Mushrooms / شرائح فطر" For the second one: "Whole Mushrooms / Whole Mushrooms / فطر كامل"). - We have to read the slogan of Mira Pomel, only in French, which is: "Vegetables are us. You're the boss!"; - the notice, in French and English: "Conditioned by SARL Velunda / Conditioned by SARL Velunda". The choice of colors is up to you, do not be afraid to think outside the box. We would like an image of the product on each particular label (on one, an image of sliced ​​mushrooms, and on the other one, an image of whole mushrooms). You will find attached the logo of the brand Mira Pomel and the label will be printed. The size of the label is 11cm X 23cm. We can not wait to see what your minds can bring!

Target Market(s)

North America

Industry/Entity Type

Food Production

Font styles to use
Script

Colors

Designer to choose colors to be used in the design.

Requirements
Must have
• - The size of the label is 11cmX23cm - the nutrition facts; you can leave a space for it or just use it for one model. - the list of ingredients (mushrooms, water, salt, citric acid); - the weight: 200 g; - For the first one: "Sliced ​​Mushrooms / Sliced ​​Mushrooms / شرائح فطر" For the second one: "Whole Mushrooms / Whole Mushrooms / فطر كامل"). - We have to read the slogan of Mira Pomel, only in French, which is: "Vegetables are us. You're the boss!"; - the notice, in French and English: "Conditioned by SARL Velunda / Conditioned by SARL Velunda".
Nice to have
• An image of mushrooms (sliced ​​and whole)

```html
<!DOCTYPE html>
<html lang="fr">
<head>
<meta charset="utf-8">
<title>Mira Pomel – Champignons entiers</title>
<link href="https://fonts.googleapis.com/css2?family=Kaushan+Script&family=Ubuntu:wght@500;700&display=swap" rel="stylesheet">
<style>
  :root {
    --backdrop: #f0d5b6;
    --brown: #7b3f22;
    --brown-dark: #6a341b;
    --green: #8cc63f;
    --green-light: #a6d65a;
    --white: #ffffff;
    --mushroom-cream: #efe4d3;
    --mushroom-shade: #c9ad8a;
    --parsley: #4f9a2e;
  }
  html, body {
    margin: 0;
    padding: 0;
    width: 1139px;
    height: 1200px;
    overflow: hidden;
    background: var(--backdrop);
  }
  .canvas {
    position: relative;
    width: 1139px;
    height: 1200px;
  }
  .label {
    position: absolute;
    left: 30px;
    top: 342px;
    width: 1079px;
    height: 516px;
    box-shadow: 0 2px 6px rgba(0,0,0,0.15);
  }
  .slogan {
    font-family: 'Kaushan Script', cursive;
    fill: var(--white);
    font-size: 44px;
  }
  .product-name {
    font-family: 'Ubuntu', sans-serif;
    font-weight: 700;
    fill: var(--white);
    font-size: 19px;
  }
  .brand-name {
    font-family: 'Ubuntu', sans-serif;
    font-weight: 700;
    fill: var(--brown);
    font-size: 26px;
  }
  .notice {
    font-family: 'Ubuntu', sans-serif;
    font-weight: 700;
    fill: var(--brown);
    font-size: 19px;
  }
  .weight {
    font-family: 'Ubuntu', sans-serif;
    font-weight: 700;
    fill: var(--white);
    font-size: 28px;
  }
  .panel-title {
    font-family: 'Ubuntu', sans-serif;
    font-weight: 500;
    fill: var(--brown);
    font-size: 11px;
  }
  .panel-body {
    font-family: 'Ubuntu', sans-serif;
    font-weight: 700;
    fill: var(--brown);
    font-size: 10.5px;
  }
</style>
</head>
<body>
<div class="canvas">
  <svg class="label" viewBox="0 0 1124 538" xmlns="http://www.w3.org/2000/svg">
    <defs>
      <radialGradient id="mushroom-tone" cx="45%" cy="40%" r="60%">
        <stop offset="0%" stop-color="var(--white)"/>
        <stop offset="70%" stop-color="var(--mushroom-cream)"/>
        <stop offset="100%" stop-color="var(--mushroom-shade)"/>
      </radialGradient>
    </defs>

    <!-- label base -->
    <rect class="label-base" x="0" y="0" width="1124" height="538" fill="var(--white)"/>

    <!-- brown top band with wavy lower edge -->
    <path class="top-band" d="M0 0 H1124 V345 C900 300 720 326 562 338 C400 350 200 300 0 352 Z" fill="var(--brown)"/>
    <path class="wave-line" d="M0 360 C200 308 400 358 562 346 C720 334 900 308 1124 353" fill="none" stroke="var(--green)" stroke-width="9"/>

    <!-- ring pattern area -->
    <rect class="ring-pattern" x="0" y="0" width="1124" height="330" fill="var(--brown)" opacity="0.0001" role="img" aria-label="Scattered white and green outline rings decorating the brown band"/>

    <!-- brand block -->
    <g class="brand-block">
      <rect x="470" y="14" width="185" height="121" rx="14" fill="var(--green)"/>
      <rect x="488" y="22" width="149" height="101" rx="8" fill="var(--white)"/>
      <text class="brand-name" x="562" y="82" text-anchor="middle">Mira Pomel</text>
    </g>

    <!-- slogan -->
    <text class="slogan" x="562" y="200" text-anchor="middle">Les légumes, c’est nous.</text>
    <text class="slogan" x="562" y="250" text-anchor="middle">Le chef, c’est vous!</text>

    <!-- product name -->
    <text class="product-name" x="562" y="298" text-anchor="middle">Champignons entiers / Whole Mushrooms / <tspan direction="rtl" unicode-bidi="embed">فطر كامل</tspan></text>

    <!-- nutrition panel -->
    <g class="nutrition-panel">
      <rect x="12" y="360" width="196" height="167" rx="14" fill="var(--white)" stroke="var(--brown)" stroke-width="1.2"/>
      <text class="panel-title" x="28" y="384">The nutrition facts:</text>
      <line x1="28" y1="388" x2="126" y2="388" stroke="var(--brown)" stroke-width="0.8"/>
    </g>

    <!-- ingredients panel -->
    <g class="ingredients-panel">
      <rect x="917" y="360" width="195" height="167" rx="14" fill="var(--white)" stroke="var(--brown)" stroke-width="1.2"/>
      <text class="panel-title" x="932" y="384">The list of ingredients:</text>
      <line x1="932" y1="388" x2="1046" y2="388" stroke="var(--brown)" stroke-width="0.8"/>
      <text class="panel-body" x="932" y="405">Mushrooms, water, salt,</text>
      <text class="panel-body" x="932" y="419">citric acid.</text>
    </g>

    <!-- notice -->
    <text class="notice" x="562" y="404" text-anchor="middle">Conditionné par SARL Velunda/Conditioned by SARL Velunda</text>

    <!-- product imagery -->
    <ellipse class="product-image" cx="388" cy="470" rx="122" ry="62" fill="url(#mushroom-tone)" role="img" aria-label="Whole white button mushrooms with a sprig of parsley"/>
    <ellipse class="product-image" cx="736" cy="470" rx="122" ry="62" fill="url(#mushroom-tone)" role="img" aria-label="Whole white button mushrooms with a sprig of parsley"/>

    <!-- weight badge -->
    <g class="weight-badge">
      <circle cx="562" cy="472" r="53" fill="var(--green)"/>
      <circle cx="562" cy="472" r="43" fill="var(--brown)"/>
      <text class="weight" x="562" y="482" text-anchor="middle">200g</text>
    </g>
  </svg>
</div>
</body>
</html>
```